National Chemical Line for Homeowners Needs a Logo & Label Design.

We need a logo and label design for a New National Chemical Company that is Private Labeling/Creating Cleaning Chemicals for Homeowners to use themselves. These chemicals will be used to clean carpets, hard surfaces, remove cat & dog stains and odors and many other products to come.
The first product will be for homeowners to remove cat & dog stains and odors from their carpets. We would like the label for the front and back of a 32 oz. white spray bottle. Go to www.brellowsupply.com and reference Part# 41KPL7.
We want the bottle/label to stand out on the grocery store shelves. We want it to be simple to read, eye catching, have a simple name and explain what the product does . The back of the bottle will have directions, caution statements, etc.
The Name of our Company is Tidal Marvels. It does have a trademark. We want the word "Tidal" to stand out and the word "marvels to only be present, that way the word Tidal will gain traction with the customer.
We want the color scheme to be Pinks & Blues.

```html
<!DOCTYPE html>
<html lang="en">
<head>
<meta charset="utf-8">
<title>Tidal Marvels – Front Label</title>
<link href="https://fonts.googleapis.com/css2?family=Montserrat:wght@400;500;600&display=swap" rel="stylesheet">
<style>
  :root {
    --canvas: #e6e6e6;
    --teal: #4fc7cb;
    --teal-light: #6fd6d8;
    --pink: #dd65a0;
    --pink-deep: #d45a96;
    --silver: #b9bcc2;
    --white: #ffffff;
    --ink-pink: #7a2450;
  }
  * { margin: 0; padding: 0; box-sizing: border-box; }
  html, body {
    width: 1200px;
    height: 1200px;
    overflow: hidden;
    background: var(--canvas);
    font-family: "Montserrat", sans-serif;
  }
  .label {
    position: absolute;
    left: 220px;
    top: 170px;
    width: 760px;
    height: 860px;
  }
  .label-shape {
    position: absolute;
    inset: 0;
  }
  .brand-name {
    position: absolute;
    top: 195px;
    left: 0;
    width: 100%;
    text-align: center;
    color: var(--white);
    font-weight: 600;
    font-size: 118px;
    letter-spacing: 6px;
    line-height: 1;
  }
  .brand-sub {
    position: absolute;
    top: 335px;
    left: 0;
    width: 100%;
    text-align: center;
    color: var(--white);
    font-weight: 400;
    font-size: 20px;
    letter-spacing: 10px;
  }
  .product-claim {
    position: absolute;
    top: 525px;
    left: 110px;
    width: 540px;
    text-align: center;
    color: var(--white);
    font-weight: 500;
    font-size: 30px;
    line-height: 1.3;
  }
  .net-content {
    position: absolute;
    top: 770px;
    left: 0;
    width: 100%;
    text-align: center;
    color: var(--ink-pink);
    font-weight: 400;
    font-size: 15px;
    line-height: 1.2;
  }
</style>
</head>
<body>
  <div class="label">
    <svg class="label-shape" width="760" height="860" viewBox="0 0 760 860">
      <defs>
        <clipPath id="label-outline">
          <rect x="0" y="0" width="760" height="860" rx="70" ry="70"/>
        </clipPath>
        <linearGradient id="teal-fill" x1="0" y1="0" x2="1" y2="1">
          <stop offset="0" stop-color="var(--teal-light)"/>
          <stop offset="1" stop-color="var(--teal)"/>
        </linearGradient>
        <linearGradient id="pink-fill" x1="0" y1="0" x2="1" y2="0">
          <stop offset="0" stop-color="var(--pink)"/>
          <stop offset="1" stop-color="var(--pink-deep)"/>
        </linearGradient>
      </defs>
      <g clip-path="url(#label-outline)">
        <rect class="label-pink" x="0" y="0" width="760" height="860" fill="url(#pink-fill)"/>
        <polygon class="label-teal" points="0,0 760,0 760,265 380,430 0,265" fill="url(#teal-fill)" role="img" aria-label="Teal panel with a faint chevron texture"/>
        <polyline class="label-chevron" points="0,272 380,437 760,272" fill="none" stroke="var(--silver)" stroke-width="12"/>
      </g>
    </svg>
    <div class="brand-name">TIDAL</div>
    <div class="brand-sub">MARVELS</div>
    <p class="product-claim">Cleaning Carpets, Hard Surfaces, Removing Cat And Dog Stains and Odors</p>
    <p class="net-content">NET WT<br>32 fl. oz (946.353)</p>
  </div>
</body>
</html>
```